Brightleaf Plots LLC business card

I created a front and back idea of what I want. Also I included my Brightleaf Plots logo to be used on the card. Please use your creativity to make it look professional and awesome! Use the all text and phrases in the sample card that I made.

(Front of card)Key words and phrases:
FOOD GROWING MACHINES
Aeroponics Technology
No soil
No pesticides
98% less water
Grow year round

(Back of card)
EVERY MONTH ONE SPIRE PLANTER WILL BE GIVEN AWAY
FOLLOW US ON IG FOR A CHANCE TO WIN A SPIRE PLANTER
FOOD GROWING MACHINES
Vertical Farming
Urban Farming
100% Organic
Grows 40% Faster
Indoors/outdoors

My contact info:
Chef Morv
Phone:555 417-3290
web: brightleafplots.example
IG: brightleafplotsxy

Target Market(s)

urban farming, vertical farming gardening

Industry/Entity Type

Gardening

Contact Information for Business Card

Front of card)Key words and phrases:
FOOD GROWING MACHINES
Aeroponics Technology
No soil
No pesticides
98% less water
Grow year round

(Back of card)
FOOD GROWING MACHINES
Vertical Farming
Urban Farming
100% Organic
Grows 40% Faster
Indoors/outdoors

My contact info:
Phone:555 417-3290
web: brightleafplots.example
IG: brightleafplotsxy

Requirements
Must have
• My contact info:
Chef Morv
Phone:555 417-3290
web: brightleafplots.example
IG: brightleafplotsxy
Nice to have
• Great imagery and easy to read. Try to incorporate the image that I uploaded of the little girl.

```html
<!DOCTYPE html>
<html lang="en">
<head>
<meta charset="utf-8">
<title>Brightleaf Plots – Business Card</title>
<link href="https://fonts.googleapis.com/css2?family=Roboto:ital,wght@0,400;0,500;0,700;0,900;1,700;1,900&display=swap" rel="stylesheet">
<style>
  :root {
    --stage: #15285a;
    --leaf: #9dca3c;
    --navy: #17213a;
    --white: #ffffff;
    --mint: #d8ebae;
    --pill-top: #ffffff;
    --pill-bottom: #b9dc7a;
  }
  * { box-sizing: border-box; margin: 0; padding: 0; }
  html, body { width: 1200px; height: 1200px; overflow: hidden; }
  body {
    background: var(--stage);
    font-family: "Roboto", Arial, sans-serif;
    position: relative;
  }
  .card {
    position: absolute;
    left: 219px;
    width: 762px;
    height: 510px;
    overflow: hidden;
  }
  .card--front { top: 50px; background: var(--leaf); }
  .card--back  { top: 623px; background: var(--navy); }

  .photo { position: absolute; left: 0; top: 0; width: 762px; height: 373px; }

  .brand-name {
    position: absolute;
    left: 476px;
    top: 62px;
    font-weight: 900;
    font-size: 44px;
    line-height: 44px;
    color: var(--navy);
    text-transform: uppercase;
    letter-spacing: 0.5px;
  }

  .headline {
    position: absolute;
    left: 50px;
    top: 54px;
    font-weight: 700;
    font-size: 37px;
    line-height: 37px;
    text-transform: uppercase;
    color: var(--navy);
  }
  .card--back .headline { color: var(--mint); }
  .card--back .headline .headline__first { color: var(--white); }

  .tech-pill {
    position: absolute;
    left: 45px;
    top: 170px;
    width: 190px;
    height: 54px;
    border-radius: 12px;
    background: linear-gradient(180deg, var(--pill-top) 35%, var(--pill-bottom));
    color: var(--navy);
    font-weight: 500;
    font-size: 19px;
    line-height: 20px;
    padding: 7px 0 0 20px;
  }
  .card--back .tech-pill { text-align: center; padding: 7px 0 0; }

  .benefits {
    position: absolute;
    list-style: none;
    font-size: 19px;
    font-weight: 400;
  }
  .card--front .benefits { left: 53px; top: 233px; color: var(--navy); }
  .card--back .benefits { left: 58px; top: 250px; color: var(--white); }
  .benefits li { display: flex; align-items: center; height: 33.5px; }
  .benefits svg { width: 18px; height: 18px; margin-right: 12px; flex: none; }
  .card--back .benefits svg { margin-right: 15px; }

  .giveaway {
    position: absolute;
    left: 0; top: 373px;
    width: 762px; height: 62px;
    text-align: center;
    text-transform: uppercase;
    font-size: 18px;
    padding-top: 5px;
    line-height: 27px;
  }
  .card--front .giveaway { background: var(--navy); color: var(--leaf); }
  .card--back .giveaway { background: var(--leaf); color: var(--white); border-bottom: 1px solid var(--white); }
  .giveaway strong { font-weight: 900; font-style: italic; }
  .giveaway .giveaway__prize { font-size: 21px; }
  .card--back .giveaway strong { color: var(--navy); }

  .contact {
    position: absolute;
    left: 0; top: 443px;
    width: 762px;
    display: flex;
    justify-content: center;
    align-items: center;
    gap: 12px;
    font-size: 19px;
    font-weight: 500;
    color: var(--white);
  }
  .contact__item { display: flex; align-items: center; gap: 5px; }
  .contact__item svg { width: 17px; height: 17px; }
  .contact__name { font-weight: 900; font-style: italic; }
  .card--front .contact__name { color: var(--navy); }
  .card--back .contact__name { color: var(--leaf); }
  .card--front .contact__item svg { stroke: var(--navy); }
  .card--back .contact__item svg { stroke: var(--white); }
</style>
</head>
<body>

<section class="card card--front">
  <svg class="photo" viewBox="0 0 762 373" role="img" aria-label="Photo of a young girl holding a metal colander beside a vertical garden tower of leafy chard">
    <defs>
      <linearGradient id="photoToneFront" x1="0" y1="0" x2="1" y2="0">
        <stop offset="0" stop-color="#c98a9a"/>
        <stop offset="0.45" stop-color="#d4c4b4"/>
        <stop offset="1" stop-color="#8fb56a"/>
      </linearGradient>
    </defs>
    <path d="M453 0 H762 V373 H281 C295 210 360 60 453 0 Z" fill="url(#photoToneFront)"/>
  </svg>
  <div class="brand-name">Brightleaf<br>Plots</div>

  <h1 class="headline">Food<br>Growing<br>Machines</h1>
  <div class="tech-pill">Aeroponics<br>Technology</div>
  <ul class="benefits">
    <li><svg viewBox="0 0 18 18"><path d="M2 10 L7 15 L16 3" fill="none" stroke="#17213a" stroke-width="3"/></svg>No soil</li>
    <li><svg viewBox="0 0 18 18"><path d="M2 10 L7 15 L16 3" fill="none" stroke="#17213a" stroke-width="3"/></svg>No pesticides</li>
    <li><svg viewBox="0 0 18 18"><path d="M2 10 L7 15 L16 3" fill="none" stroke="#17213a" stroke-width="3"/></svg>98% less water</li>
    <li><svg viewBox="0 0 18 18"><path d="M2 10 L7 15 L16 3" fill="none" stroke="#17213a" stroke-width="3"/></svg>Grow year round</li>
  </ul>

  <div class="giveaway">
    Every month one spire planter will be given away<br>
    <strong>Follow us on IG</strong> for a chance to <strong class="giveaway__prize">Win a spire planter</strong>
  </div>

  <div class="contact">
    <span class="contact__name">Chef Morv</span>
    <span class="contact__item"><svg viewBox="0 0 18 18"><path d="M4 2 L7 2 L8 6 L6 7.5 C7 10 8 11 10.5 12 L12 10 L16 11 L16 14 C16 15 15 16 14 16 C8 16 2 10 2 4 C2 3 3 2 4 2 Z" fill="none" stroke-width="1.8"/></svg>555 417-3290</span>
    <span class="contact__item"><svg viewBox="0 0 18 18" fill="none" stroke-width="1.6"><circle cx="9" cy="9" r="7.5"/><ellipse cx="9" cy="9" rx="3.2" ry="7.5"/><path d="M1.5 9 H16.5 M3 5 H15 M3 13 H15"/></svg>brightleafplots.example</span>
    <span class="contact__item"><svg viewBox="0 0 18 18" fill="none" stroke-width="1.8"><circle cx="9" cy="9" r="7"/></svg>brightleafplotsxy</span>
  </div>
</section>

<section class="card card--back">
  <svg class="photo" viewBox="0 0 762 373" role="img" aria-label="Photo of a young girl holding a metal colander beside a vertical garden tower of leafy chard">
    <defs>
      <linearGradient id="photoToneBack" x1="0" y1="0" x2="1" y2="0">
        <stop offset="0" stop-color="#c98a9a"/>
        <stop offset="0.45" stop-color="#d4c4b4"/>
        <stop offset="1" stop-color="#8fb56a"/>
      </linearGradient>
    </defs>
    <path d="M453 0 H762 V373 H281 C295 210 360 60 453 0 Z" fill="url(#photoToneBack)"/>
  </svg>
  <div class="brand-name">Brightleaf<br>Plots</div>

  <h1 class="headline"><span class="headline__first">Food</span><br>Growing<br>Machines</h1>
  <div class="tech-pill">Vertical Farming<br>Urban Farming</div>
  <ul class="benefits">
    <li><svg viewBox="0 0 18 18"><path d="M2 10 L7 15 L16 3" fill="none" stroke="#9dca3c" stroke-width="3"/></svg>100% Organic</li>
    <li><svg viewBox="0 0 18 18"><path d="M2 10 L7 15 L16 3" fill="none" stroke="#9dca3c" stroke-width="3"/></svg>Grows 40% Faster</li>
    <li><svg viewBox="0 0 18 18"><path d="M2 10 L7 15 L16 3" fill="none" stroke="#9dca3c" stroke-width="3"/></svg>Indoors/outdoors</li>
  </ul>

  <div class="giveaway">
    Every month one spire planter will be given away<br>
    <strong>Follow us on IG</strong> for a chance to <strong class="giveaway__prize">Win a spire planter</strong>
  </div>

  <div class="contact">
    <span class="contact__name">Chef Morv</span>
    <span class="contact__item"><svg viewBox="0 0 18 18"><path d="M4 2 L7 2 L8 6 L6 7.5 C7 10 8 11 10.5 12 L12 10 L16 11 L16 14 C16 15 15 16 14 16 C8 16 2 10 2 4 C2 3 3 2 4 2 Z" fill="none" stroke-width="1.8"/></svg>555 417-3290</span>
    <span class="contact__item"><svg viewBox="0 0 18 18" fill="none" stroke-width="1.6"><circle cx="9" cy="9" r="7.5"/><ellipse cx="9" cy="9" rx="3.2" ry="7.5"/><path d="M1.5 9 H16.5 M3 5 H15 M3 13 H15"/></svg>brightleafplots.example</span>
    <span class="contact__item"><svg viewBox="0 0 18 18" fill="none" stroke-width="1.8"><circle cx="9" cy="9" r="7"/></svg>brightleafplotsxy</span>
  </div>
</section>

</body>
</html>
```